Website Design - for Energy Efficiency company - large corporate feel

Hi there,
Thanks for checking out this project!
We're a UK based energy efficiency business. We arrange for energy efficient systems to be fitted in people's houses (i.e. efficient boilers, solar panels etc.) However, we do not install them ourselves as we have accredited installers who install on our behalf. Therefore the website should appeal to these businesses and have a very professional corporate feel. The final design should communicate that we are a financially safe large corporation.
Our existing website should not be used for inspiration as the style and content are very outdated (it was from a time when were installers - which we no longer are).
The new website design should use the greens from our logo, however I don't want the site saturated in this colour.
I'm really open to your chosen layout and therefore I'm not a huge fan of including links to websites I like - as I don't want to limit your own creativity. However, I would like it to look corporate (but not too boring and unimaginative).
So here's a few links to websites that I feel give a feel of financially safe / large corporate etc. Although you certainly don't have to design with this style / layout in mind:
http://www.brenholt.org.uk/advice
http://www.tavishworks.co.uk/
http://www.dqvb.org.uk/
http://www.orrinlodgeway.co.uk/
http://www.pkwynd.co.uk/ (very bad design but looks corporate)
http://www.ferrowmoor.org.uk/
http://www.tq.co.uk/ (looks corporate but too busy and boring)
http://www.quellaro.co.uk/business/index.htm
http://www.mobrevo.com/
https://www.tervold.com/en/index.html
The site is for 4 different audiences:
Consumers | Businesses | Public Sector | Installers
Therefore, it's important that there is some form of way of splitting the site up into these sections (almost like 4 websites in 1). Each section will then have the navigation menu with 7 links.
I've attached our logo (company-logo.jpg) and another logo design we have to display inline with regulations (fair-loan-logo.jpg).
Happy designing, and thank you!

```html
<!DOCTYPE html>
<html lang="en">
<head>
<meta charset="utf-8">
<title>Leafmere Energy</title>
<link rel="stylesheet" href="https://fonts.googleapis.com/css2?family=Open+Sans:ital,wght@0,400;0,600;1,400&family=Roboto+Condensed:wght@400&family=Mulish:wght@200;300;400&display=swap">
<style>
:root{
  --green:#7cb82f;
  --green-dark:#4f8f1c;
  --green-light:#a6d54a;
  --ink:#333;
  --muted:#555;
  --line:#d9d9d9;
  --footer:#3a3a3a;
  --footer-bottom:#2e2e2e;
  --footer-text:#cfcfcf;
}
*{margin:0;padding:0;box-sizing:border-box}
html,body{width:880px;height:1200px;overflow:hidden;background:#fff}
body{position:relative;font-family:"Open Sans",sans-serif;color:var(--ink)}
.abs{position:absolute}

/* header */
.brand{left:70px;top:32px;display:flex;align-items:center;gap:8px}
.brand-mark{width:46px;height:46px;border-radius:50%;background:var(--green)}
.brand-name{font-family:"Open Sans",sans-serif;font-weight:600;font-size:33px;color:var(--green-dark);letter-spacing:-0.5px;line-height:1}
.callus{right:70px;top:38px;font-size:12px;color:#555;font-weight:600}
.socials{right:70px;top:60px;display:flex;gap:8px}
.socials span{width:18px;height:18px;border-radius:50%;background:#8d8d8d}

/* nav */
.nav{left:0;top:92px;width:880px;height:30px;background:linear-gradient(#8fc63d,#6aa626)}
.nav ul{list-style:none;display:flex;position:absolute;left:66px;top:0;height:30px}
.nav li{font-family:"Roboto Condensed",sans-serif;color:#fff;font-size:12px;line-height:30px;padding:0 13px;border-right:1px solid rgba(0,0,0,.12)}
.nav li:last-child{border-right:none}
.search{left:650px;top:98px;width:147px;height:19px;border-radius:10px;background:#fff;border:1px solid #cde6a8;font-size:9px;color:#777;padding:3px 0 0 7px}
.search i{position:absolute;right:3px;top:2px;width:13px;height:13px;border-radius:50%;background:var(--green)}

/* hero */
.hero{left:0;top:122px;width:880px;height:295px;background:linear-gradient(90deg,#7fa9cf 0%,#9cc0dd 40%,#b7cfe2 100%)}
.hero-scene{position:absolute;left:380px;top:0;width:500px;height:295px;background:linear-gradient(160deg,#b8cfe0 0%,#8aa0b2 55%,#3f5a7a 100%)}
.hero-title{left:72px;top:186px;font-family:"Mulish",sans-serif;font-weight:200;font-size:37px;color:#fff;letter-spacing:-1px}
.hero-title em,.hero-sub em{font-style:normal;color:var(--green-light)}
.hero-sub{left:79px;top:232px;font-family:"Mulish",sans-serif;font-weight:300;font-size:21px;color:#fff;letter-spacing:-0.8px}
.hero-copy{left:82px;top:266px;width:300px;font-size:9.5px;line-height:21px;color:#222}
.btn{background:linear-gradient(#7cbb36,#5c9a20);color:#fff;border-radius:2px}
.hero-btn{left:79px;top:331px;width:82px;height:26px;font-size:12px;line-height:26px;text-align:center}
.dots{left:80px;top:371px;display:flex;gap:3px}
.dots span{width:9px;height:9px;border-radius:50%;background:var(--green);border:1px solid #fff}
.dots span:first-child{background:#e8f5d0}

/* audiences */
.audiences{left:72px;top:417px;width:728px;height:145px;display:flex}
.aud{flex:1;text-align:center;border-right:1px solid #eee;padding-top:28px}
.aud:last-child{border-right:none}
.aud svg{height:44px}
.aud h3{font-family:"Mulish",sans-serif;font-weight:400;font-size:14px;color:var(--green-dark);margin-top:4px}
.aud p{font-size:8.3px;line-height:16px;color:#333;margin-top:2px}

/* welcome */
.welcome{left:80px;top:586px;width:482px}
.sec-title{font-family:"Mulish",sans-serif;font-weight:400;font-size:16px;color:var(--green-dark);letter-spacing:-0.4px;padding-bottom:3px;border-bottom:1px dotted #bbb;position:relative}
.sec-title b{font-weight:400;color:#222}
.sec-title::after{content:"";position:absolute;left:0;bottom:-3px;width:106px;height:3px;background:var(--green)}
.arrows{position:absolute;right:2px;top:6px;display:flex;gap:2px}
.arrows span{width:12px;height:12px;background:#eee}
.welcome p{font-size:8.8px;line-height:14px;color:#444;margin-top:14px}
.welcome p+p{margin-top:13px}
.welcome .btn{display:inline-block;margin-top:16px;font-size:9.5px;padding:4px 10px}

.testi{left:576px;top:586px;width:220px}
.testi h2{font-family:"Mulish",sans-serif;font-weight:400;font-size:15px;color:var(--green-dark)}
.quote{margin-top:15px;margin-left:2px;border:1px solid #ccc;border-radius:2px;padding:10px 12px;font-style:italic;font-size:8.6px;line-height:14px;color:#444;position:relative}
.quote::after{content:"";position:absolute;left:18px;bottom:-11px;width:12px;height:12px;background:#fff;border-left:1px solid #ccc;transform:skewY(-45deg)}
.testi .who{font-size:8.8px;margin:12px 0 0 33px;color:#333}

/* clients */
.clients{left:78px;top:806px;width:716px}
.clients .sec-title::after{width:104px}
.client-row{left:84px;top:854px;width:680px;height:38px}
.badge{position:absolute;background:#b8b8b8}

/* footer */
.footer{left:0;top:953px;width:880px;height:212px;background:var(--footer)}
.fcol{position:absolute;top:37px;color:var(--footer-text)}
.fcol h4{font-weight:400;font-size:10px;color:#fff;letter-spacing:.2px;margin-bottom:17px}
.fcol p{font-size:8.3px;line-height:14px}
.contact-list{font-size:8.3px;line-height:15px}
.contact-list .row{display:flex;align-items:center;gap:7px;margin-top:3px}
.contact-list svg{width:10px;height:10px}
.fsocial{display:flex;gap:4px;margin-top:14px}
.fsocial span{width:30px;height:30px;background:#333;border:1px solid #3f3f3f}
.fsocial span.on{background:#777}
.flogo{position:absolute;left:641px;top:170px;display:flex;align-items:center;gap:5px}
.flogo i{width:24px;height:24px;border-radius:50%;background:#6f6f6f}
.flogo span{font-size:18px;font-weight:600;color:#8a8a8a}
.fbottom{left:0;top:1165px;width:880px;height:35px;background:var(--footer-bottom);font-size:8.3px;color:#cfcfcf}
.top-tab{position:absolute;left:427px;top:-12px;width:38px;height:24px;border-radius:19px 19px 0 0;background:var(--footer-bottom)}
.top-tab svg{position:absolute;left:14px;top:7px}
</style>
</head>
<body>

<header>
  <div class="abs brand"><span class="brand-mark"></span><span class="brand-name">Leafmere Energy</span></div>
  <div class="abs callus">Call Us : (1)120 555 019</div>
  <div class="abs socials"><span></span><span></span><span></span><span></span><span></span><span></span></div>
</header>

<nav class="abs nav">
  <ul>
    <li>LEAFMERE</li><li>HOME OWNERS</li><li>SPACER TENANTS</li><li>SPACER LANDLORDS</li><li>BOOKING</li><li>CONTACT US</li>
  </ul>
</nav>
<div class="abs search">Search<i></i></div>

<section class="abs hero">
  <div class="hero-scene" role="img" aria-label="Photo: two engineers in hard hats reviewing plans beside rooftop solar panels"></div>
</section>
<h1 class="abs hero-title">The Green <em>Deal funding.</em></h1>
<div class="abs hero-sub">CONSUME ANYTHING <em>YOU WANT</em></div>
<p class="abs hero-copy">Le Lorem Ipsum est simplement du faux texte employé dans la composition et la mise en page avant impression. Le Lorem Ipsum , quand un peintre anonyme assembla ensemble des morceaux de</p>
<div class="abs btn hero-btn">Read More</div>
<div class="abs dots"><span></span><span></span><span></span></div>

<section class="abs audiences">
  <div class="aud">
    <svg viewBox="0 0 40 44"><path d="M2 2h36v28H12l-10 12z" fill="#7cb82f"/><rect x="10" y="14" width="4" height="12" fill="#fff"/><rect x="17" y="8" width="4" height="18" fill="#fff"/><rect x="24" y="16" width="4" height="10" fill="#fff"/></svg>
    <h3>Consumers</h3>
    <p>Lorem ipsum dolor sit amet, consectetur g<br>eiusmod tempor incididunt ut labore</p>
  </div>
  <div class="aud">
    <svg viewBox="0 0 46 44"><path d="M23 2 44 14H2z" fill="#7cb82f"/><rect x="3" y="16" width="40" height="4" fill="#7cb82f"/><rect x="7" y="22" width="4" height="14" fill="#7cb82f"/><rect x="15" y="22" width="4" height="14" fill="#7cb82f"/><rect x="27" y="22" width="4" height="14" fill="#7cb82f"/><rect x="35" y="22" width="4" height="14" fill="#7cb82f"/><rect x="2" y="38" width="42" height="4" fill="#7cb82f"/></svg>
    <h3>Businesses</h3>
    <p>Lorem ipsum dolor sit amet, consectetur g<br>eiusmod tempor incididunt ut labore</p>
  </div>
  <div class="aud">
    <svg viewBox="0 0 66 44"><circle cx="14" cy="12" r="6" fill="#7cb82f"/><circle cx="52" cy="12" r="6" fill="#7cb82f"/><circle cx="33" cy="10" r="8" fill="#7cb82f"/><path d="M2 34c0-10 24-10 24 0z" fill="#7cb82f"/><path d="M40 34c0-10 24-10 24 0z" fill="#7cb82f"/><path d="M17 40c0-16 32-16 32 0z" fill="#7cb82f"/></svg>
    <h3>Public Sector</h3>
    <p>Lorem ipsum dolor sit amet, consectetur g<br>eiusmod tempor incididunt ut labore</p>
  </div>
  <div class="aud">
    <svg viewBox="0 0 46 48"><rect x="2" y="2" width="40" height="32" fill="#7cb82f"/><g stroke="#fff" stroke-width="2"><line x1="2" y1="10" x2="42" y2="10"/><line x1="2" y1="18" x2="42" y2="18"/><line x1="2" y1="26" x2="42" y2="26"/><line x1="14" y1="2" x2="14" y2="34"/></g><line x1="42" y1="20" x2="42" y2="44" stroke="#7cb82f" stroke-width="2"/></svg>
    <h3>Installers</h3>
    <p>Lorem ipsum dolor sit amet, consectetur g<br>eiusmod tempor incididunt ut labore</p>
  </div>
</section>

<section class="abs welcome">
  <h2 class="sec-title">Welcome to Green <b>Leafmere Energy</b><span class="arrows"><span></span><span></span></span></h2>
  <p>Le Lorem Ipsum est simplement du faux texte employé dans la composition et la mise en page avant impression. Le Lorem Ipsum est le faux texte standard de l'imprimerie depuis les années 1500, quand un peintre anonyme assembla ensemble des morceaux de texte pour réaliser un livre spécimen de polices de texte.</p>
  <p>Il n'a pas fait que survivre cinq siècles, mais s'est aussi adapté à la bureautique informatique, sans que son contenu n'en soit modifié. Il a été popularisé dans les années 1960 grâce à la vente de feuilles Letraset contenant des passages du Lorem Ipsum, et, plus récemment, par son.</p>
  <span class="btn">Read More</span>
</section>

<aside class="abs testi">
  <h2>Testimonials</h2>
  <div class="quote">On sait depuis longtemps que travailler avec du texte lisible et contenant du sens est source de distractions, et empêche de se concentrer sur la mise en page elle-même. L'avantage du Lorem Ipsum sur un texte.</div>
  <div class="who">Corin Waddell</div>
</aside>

<section class="abs clients">
  <h2 class="sec-title">Our <b>Clients.</b><span class="arrows"><span></span><span></span></span></h2>
</section>
<div class="abs client-row" aria-label="Accreditation badges">
  <div class="badge" style="left:0;top:8px;width:66px;height:26px;border-radius:13px"></div>
  <div class="badge" style="left:130px;top:4px;width:30px;height:30px;clip-path:polygon(100% 0,100% 100%,0 100%)"></div>
  <div class="badge" style="left:236px;top:6px;width:42px;height:26px;border-radius:50%"></div>
  <div class="badge" style="left:355px;top:4px;width:28px;height:28px;border-radius:50%"></div>
  <div class="badge" style="left:442px;top:8px;width:80px;height:24px"></div>
  <div class="badge" style="left:580px;top:2px;width:92px;height:32px;border-radius:3px"></div>
</div>

<footer class="abs footer">
  <div class="fcol" style="left:84px;width:160px">
    <h4>WHO WE ARE</h4>
    <p>Lorem ipsum dolor sit amet, consectetuer adipiscing elit. Aenean commodo ligula eget dolor. Aenean massa. Cum sociis natoque penatibus et magnis felis, ultricies nec sociis natoque penatibus et magnis felis, ultricies nec.</p>
  </div>
  <div class="fcol" style="left:268px;width:160px">
    <h4>WHAT WE DO</h4>
    <p style="line-height:18.5px">Lorem ipsum dolor sit amet, consectetuer adipiscing elit. Aenean commodo ligula eget dolor. Aenean massa. Cum sociis natoque penatibus massa. Cum sociis natoque penatibus</p>
  </div>
  <div class="fcol" style="left:470px;width:140px">
    <h4>CONTACT US</h4>
    <div class="contact-list">
      <div>Eastmere</div>
      <div>Harlow Vale&nbsp;&nbsp;&nbsp;555-201-0147</div>
      <div>Brisk Harbor&nbsp;&nbsp;555-302-0199</div>
      <div class="row"><svg viewBox="0 0 10 10"><path d="M2 1l2 2-1 1c1 2 2 3 3 3l1-1 2 2-1 2C4 10 0 6 0 3z" fill="#aaa"/></svg>1-800-555-0162</div>
      <div class="row"><svg viewBox="0 0 10 10"><rect x="0" y="2" width="10" height="7" fill="#aaa"/></svg>www.leafmere-energy.com</div>
      <div class="row"><svg viewBox="0 0 10 10"><rect x="0" y="2" width="10" height="7" fill="#aaa"/><path d="M0 2l5 4 5-4" stroke="#3a3a3a" fill="none"/></svg>info@leafmere-energy.com</div>
    </div>
  </div>
  <div class="fcol" style="left:619px;width:170px">
    <h4>GET IN TOUCH</h4>
    <p style="font-size:7.8px;line-height:15px;color:#aaa">If you ahve any questions you can conatct us via our contact form here, or follow us on social networks.</p>
    <div class="fsocial"><span></span><span></span><span></span><span class="on"></span><span></span></div>
  </div>
  <div class="flogo"><i></i><span>Leafmere Energy</span></div>
</footer>

<div class="abs fbottom">
  <div class="top-tab"><svg width="10" height="9" viewBox="0 0 10 9"><path d="M5 0 10 5H7v4H3V5H0z" fill="#999"/></svg></div>
  <span class="abs" style="left:83px;top:12px">Copyright © 2013 Leafmere Energy Ltd All Rights Reserved</span>
  <span class="abs" style="left:615px;top:11px">Terms &amp; Condition&nbsp;&nbsp;&nbsp;&nbsp;&nbsp;&nbsp;&nbsp;|&nbsp;&nbsp;&nbsp;&nbsp;&nbsp;&nbsp;&nbsp;Privacy Policy</span>
</div>

</body>
</html>
```